FlareBo Intro, Outro and Banner

I am looking for a simple FlareBo intro and outro. The into I would simply like my logo (to be provided) to appear social media logos at the bottom. Essentially this will be a graphic design that I use for an intro.

The outro I would like to have social media logos and the word subscribe. Also the words “check out my latest uploads” and two boxes where I can insert clips of my video into it (the design is just a graphic) This outro essential is a graphic design.

The last item I am looking for is a FlareBo banner that has my logo (to be provided) and social media logos and my photo with “lifestyle, business & more”. And of course “new videos weekly”.

Industry/Entity Type

Flarebo

Font styles to use
Script

Requirements
Must have
• The FlareBo banner must have my social media.
• Plimwerk, korvalume, Dorniquet and brellox are all @mirotsevin
Nice to have
• I attached an example of a layout that would be nice.

```html
<!DOCTYPE html>
<html lang="en">
<head>
<meta charset="utf-8">
<title>FlareBo Outro – Thanks for Watching</title>
<link rel="stylesheet" href="https://fonts.googleapis.com/css2?family=Righteous&family=Monoton&family=Lobster&family=Fredoka:wght@500;600&display=swap">
<style>
  :root {
    --yellow-bright: #fbfb6a;
    --yellow-base: #f2f20a;
    --yellow-edge: #ebe004;
    --red-band: #b51c12;
    --red-slot: #b61c12;
    --frame-white: #fbf6f7;
    --ink-black: #111111;
    --title-white: #ffffff;
    --script-purple: #4b1768;
    --handle-blue: #3a1fd6;
    --photo-dark: #1c2a38;
    --photo-mid: #5a5a66;
    --photo-top: #e6d6cf;
  }
  html, body {
    margin: 0;
    padding: 0;
    width: 1200px;
    height: 1200px;
    overflow: hidden;
  }
  .outro {
    position: relative;
    width: 1200px;
    height: 1200px;
    overflow: hidden;
  }
  .backdrop {
    position: absolute;
    inset: 0;
    background: radial-gradient(circle at 48% 52%, var(--yellow-bright) 0%, var(--yellow-base) 55%, var(--yellow-edge) 100%);
  }
  .title {
    position: absolute;
    top: 98px;
    left: 0;
    width: 1180px;
    margin: 0;
    text-align: center;
    font-family: "Righteous", sans-serif;
    font-weight: 400;
    font-size: 68px;
    letter-spacing: 2px;
    color: var(--title-white);
    -webkit-text-stroke: 3px var(--ink-black);
    paint-order: stroke fill;
    text-shadow: 3px 4px 0 rgba(0,0,0,0.35);
  }
  .subscribe-band {
    position: absolute;
    top: 270px;
    left: -20px;
    width: 452px;
    height: 104px;
    background: var(--red-band);
    transform: rotate(-2.3deg);
    box-shadow: 6px 8px 14px rgba(0,0,0,0.35);
  }
  .subscribe-label {
    position: absolute;
    top: 286px;
    left: 60px;
    font-family: "Monoton", sans-serif;
    font-size: 43px;
    color: var(--frame-white);
    transform: rotate(-2.3deg);
    letter-spacing: 1px;
  }
  .uploads-heading {
    position: absolute;
    top: 234px;
    left: 583px;
    margin: 0;
    font-family: "Lobster", cursive;
    font-weight: 400;
    font-size: 48px;
    color: var(--script-purple);
    text-shadow: 2px 2px 0 #ffffff;
  }
  .clip-slot {
    position: absolute;
    left: 586px;
    width: 484px;
    height: 264px;
    border: 13px solid var(--frame-white);
    background: var(--red-slot);
  }
  .clip-slot.first { top: 337px; }
  .clip-slot.second { top: 668px; }
  .host-photo {
    position: absolute;
    left: 0;
    top: 440px;
    width: 512px;
    height: 760px;
    border-radius: 46% 40% 0 0 / 28% 24% 0 0;
    background: linear-gradient(180deg, var(--photo-dark) 0%, var(--photo-mid) 55%, var(--photo-top) 85%, var(--photo-top) 100%);
  }
  .socials {
    position: absolute;
    top: 1038px;
    left: 640px;
    width: 420px;
    display: flex;
    justify-content: space-between;
    font-family: "Fredoka", sans-serif;
    font-weight: 600;
    font-size: 21px;
    color: var(--ink-black);
  }
  .socials span {
    display: flex;
    align-items: center;
    gap: 5px;
  }
  .socials span::before {
    content: "";
    width: 11px;
    height: 11px;
    border-radius: 50%;
    background: var(--ink-black);
  }
  .handle {
    position: absolute;
    top: 1090px;
    left: 640px;
    width: 440px;
    text-align: center;
    font-family: "Fredoka", sans-serif;
    font-weight: 600;
    font-size: 64px;
    color: var(--handle-blue);
  }
</style>
</head>
<body>
<main class="outro">
  <div class="backdrop" role="img" aria-label="Bright yellow background with a scattered pattern of darker yellow squares"></div>

  <h1 class="title">THANKS FOR WATCHING</h1>

  <div class="subscribe-band"></div>
  <div class="subscribe-label">SUBSCRIBE</div>

  <h2 class="uploads-heading">Check Out my latest uploads</h2>
  <div class="clip-slot first"></div>
  <div class="clip-slot second"></div>

  <div class="host-photo" role="img" aria-label="Cut-out portrait photo of the channel host with long dark wavy hair and a light top"></div>

  <div class="socials">
    <span>Plimwerk</span>
    <span>Dorniquet</span>
    <span>korvalume</span>
    <span>brellox</span>
  </div>
  <div class="handle">@mirotsevin</div>
</main>
</body>
</html>
```